UK vitamin company needs a packaging label design for new vitamin range

We have a logo, and we have the product. We now need some beautiful labels to go on the boxes which bring the product range to life.
We have 7 categories: Joint Care, Heart Heath, Brain Function, Immune System, Skin, Antioxidants and Probiotics. Each of these categories should have its own look within the plucky vitamin range. This can be quite subtle, but needs to be clearly visible and should be linked to the category e.g. 'Heart Health' might have a heart etc.
I have uploaded the logo, an example of the pack shape, and the sizing info for the label.
We are a fun brand, so please have some fun with this. We want the labels to be bold, and differentiated from the rest of the category.
Thanks
All images used must be 'rights free'. Many thanks
UK
It Company

```html
<!DOCTYPE html>
<html lang="en">
<head>
<meta charset="utf-8">
<title>Plucky Vitamins – Label Range</title>
<link href="https://fonts.googleapis.com/css2?family=Oswald:wght@300;400;500;600&display=swap" rel="stylesheet">
<style>
  :root {
    --backdrop: #4b5055;
    --paper: #ffffff;
    --ink: #4a4a4a;
    --brand-orange: #f27a22;
    --antioxidant: #8f98c3;
    --probiotic: #90c2b9;
  }
  * { margin: 0; padding: 0; box-sizing: border-box; }
  html, body { width: 1200px; height: 1200px; overflow: hidden; }
  body { background: var(--backdrop); position: relative; font-family: "Oswald", sans-serif; }

  .label {
    position: absolute; top: 130px; width: 540px; height: 912px;
    background: var(--paper); overflow: hidden;
  }
  .label--antioxidants { left: 43px; --accent: var(--antioxidant); }
  .label--probiotics { left: 620px; --accent: var(--probiotic); }

  .label__bands { position: absolute; inset: 0; width: 540px; height: 912px; }
  .label__bands path { fill: var(--accent); }

  .brand-name {
    position: absolute; top: 62px; left: 0; width: 100%; text-align: center;
    font-family: "Oswald", sans-serif; font-weight: 500; font-size: 64px;
    color: var(--brand-orange); line-height: 1; letter-spacing: 1px;
  }

  .category-title {
    position: absolute; top: 322px; left: 0; width: 100%; text-align: center;
    font-weight: 600; font-size: 66px; line-height: 1; letter-spacing: 7px;
    color: var(--ink); padding-left: 7px;
  }

  .category-icon {
    position: absolute; top: 414px; left: 178px; width: 200px; height: 180px;
    background: var(--accent);
  }

  .tagline {
    position: absolute; top: 598px; left: 170px; width: 216px; text-align: center;
    font-weight: 500; font-size: 30px; line-height: 1; color: var(--ink);
  }

  .description {
    position: absolute; top: 724px; left: 133px; width: 298px;
    font-weight: 300; font-size: 10px; line-height: 12.5px;
    text-transform: uppercase; text-align: justify; text-align-last: justify;
    color: var(--accent);
  }

  .count {
    position: absolute; top: 825px; left: 0; width: 100%; text-align: center;
    line-height: 1; color: var(--ink); font-weight: 500;
  }
  .count__number { font-size: 40px; color: var(--paper); letter-spacing: 1px; }
  .count__unit { font-size: 22px; margin-left: 4px; }
</style>
</head>
<body>

  <section class="label label--antioxidants">
    <svg class="label__bands" viewBox="0 0 540 912" aria-hidden="true">
      <path d="M0 0 H540 V37 Q270 -1 0 37 Z"/>
      <path d="M0 793 Q270 837 540 793 V912 H0 Z"/>
    </svg>
    <div class="brand-name">plucky vitamins</div>
    <h1 class="category-title">ANTIOXIDANTS</h1>
    <div class="category-icon" role="img" aria-label="White molecule icon of three joined hexagons on a lavender tile"></div>
    <p class="tagline">NATUREL ELEMENTS</p>
    <p class="description">Lorem ipsum dolor sit amet, consectetur adipiscing elit. Maecenas ullamcorper ligula non nibh rutrum, eu viverra nisl tempor. Curabitur sit amet enim eleifend, faucibus sem non, feugiat sem. Cras quis vulputate libero, vitae aliquam lorem. Aenean finibus, metus eget venenatis tempus, odio libero gravida nulla, at hendrerit nisi risus sed nisl. Mauris feugiat</p>
    <p class="count"><span class="count__number">60</span><span class="count__unit">SOFTGELS</span></p>
  </section>

  <section class="label label--probiotics">
    <svg class="label__bands" viewBox="0 0 540 912" aria-hidden="true">
      <path d="M0 0 H540 V37 Q270 -1 0 37 Z"/>
      <path d="M0 793 Q270 837 540 793 V912 H0 Z"/>
    </svg>
    <div class="brand-name">plucky vitamins</div>
    <h1 class="category-title">PROBIOTICS</h1>
    <div class="category-icon" role="img" aria-label="White outline icon of intestines inside a circle on a sea-green tile"></div>
    <p class="tagline">NATUREL ELEMENTS</p>
    <p class="description">Lorem ipsum dolor sit amet, consectetur adipiscing elit. Maecenas ullamcorper ligula non nibh rutrum, eu viverra nisl tempor. Curabitur sit amet enim eleifend, faucibus sem non, feugiat sem. Cras quis vulputate libero, vitae aliquam lorem. Aenean finibus, metus eget venenatis tempus, odio libero gravida nulla, at hendrerit nisi risus sed nisl. Mauris feugiat</p>
    <p class="count"><span class="count__number">60</span><span class="count__unit">SOFTGELS</span></p>
  </section>

</body>
</html>
```